Private Lending Company looking to have 3 Word Documents re-formatted, cleaned up and generally made

We have three word documents that we use for presentations.
a) The first document (Wholesale and Portfolio Investor Pack May 2016) has graphs incorporated which are currently blurred and perhaps not the most current data. All graphs have the source noted so these would need to be replaced with current data if it is available and generally cleaned up. The cover page requires our new logo (attached). The illustration on page 29 needs to be changed to a matrix or cube or something that represents/brings all the elements of page 29 (ie 4 bullet points) together. The whole document needs to look more corporate and professional.
b) The second and third documents (Talvora KRB Lending Guides July 2016 and Talvora Select Lending Guides July 2016) both require tidying up. Tables are not quite aligned, data within the tables is not lined up or consistent. Again, both documents need to be polished and given to look more corporate. Ensure the logo in the letterhead is the same size on each page.
Throughout all documents it is important to keep tables, shading, size etc consistent. Any table fill should be in the same blue (as per advert) throughout Documents 2 & 3.
We would like our corporate colours to be used not only in the letterhead but also in the font, the fill in the tables etc.
We have attached our logo, and a digital copy of an advert we recently used. The advert is attached more for your information - you do not need to use it at all.
The colours used in the advert are as follows:
Blue - RGB: R=30, G=30, B=59
Gold - RGB: R=227, G=205, B=152 (for table outlines)
Blue - CMYK: C=97%, M=87%, Y=45%, K=55%
Gold - CMYK: C=12%, M=21%, Y=51%, K=2% (for table outlines)
The blue in our logo is on the standard Word Pallette (Dark Blue, Text 2, Darker 25%)
The light blue featured in the tables of Document 1 can be: Blue, Accent 1, Lighter 80%. This also needs to be used consistently thoughout this document.
We would like all text to be in the same colour as the logo, although of course not necessarily the same font. Our preferred Font is Century Gothic.
Please direct any questions back to us.
It Company
- Calibri

```html
<!DOCTYPE html>
<html lang="en">
<head>
<meta charset="utf-8">
<title>Governance Structure</title>
<link href="https://fonts.googleapis.com/css2?family=Montserrat:wght@700&family=Questrial&display=swap" rel="stylesheet">
<style>
  :root {
    --canvas: #ffffff;
    --board-blue: #3c6391;
    --navy: #1f1f3a;
    --panel: #dde5ee;
    --panel-text: #2b3346;
    --connector: #24243f;
    --on-dark: #ffffff;
  }
  * { margin: 0; padding: 0; box-sizing: border-box; }
  html, body {
    width: 1200px;
    height: 676px;
    overflow: hidden;
    background: var(--canvas);
  }
  .org-chart {
    position: relative;
    width: 1200px;
    height: 676px;
  }
  .connectors {
    position: absolute;
    inset: 0;
  }
  .node {
    position: absolute;
    display: flex;
    align-items: center;
    justify-content: center;
    text-align: center;
  }
  .node--primary {
    font-family: "Montserrat", sans-serif;
    font-weight: 700;
    font-size: 36px;
    letter-spacing: 0.5px;
    color: var(--on-dark);
  }
  .node--board { left: 339px; top: 58px; width: 518px; height: 81px; background: var(--board-blue); }
  .node--management { left: 339px; top: 536px; width: 518px; height: 83px; background: var(--navy); }
  .node--support {
    font-family: "Questrial", sans-serif;
    font-size: 30px;
    line-height: 1.22;
    color: var(--panel-text);
    background: var(--panel);
    width: 231px;
    height: 152px;
  }
  .node--secretary { left: 45px; top: 58px; width: 225px; }
  .node--audit { left: 943px; top: 58px; }
  .node--lending { left: 943px; top: 259px; }
  .node--compliance { left: 943px; top: 470px; }
</style>
</head>
<body>
<main class="org-chart" aria-label="Governance structure">
  <svg class="connectors" width="1200" height="676" viewBox="0 0 1200 676" aria-hidden="true">
    <defs>
      <marker id="arrowhead" viewBox="0 0 10 10" refX="9" refY="5" markerWidth="6" markerHeight="6" orient="auto-start-reverse">
        <path d="M0 0 L10 5 L0 10 Z" fill="var(--connector)"/>
      </marker>
    </defs>
    <g stroke="var(--connector)" stroke-width="3.5" fill="none">
      <line x1="270" y1="99" x2="337" y2="99" marker-end="url(#arrowhead)"/>
      <line x1="600" y1="536" x2="600" y2="141" marker-end="url(#arrowhead)"/>
      <line x1="943" y1="99" x2="859" y2="99" marker-end="url(#arrowhead)"/>
      <line x1="900" y1="99" x2="900" y2="574"/>
      <line x1="943" y1="336" x2="902" y2="336" marker-start="url(#arrowhead)"/>
      <line x1="943" y1="574" x2="902" y2="574" marker-start="url(#arrowhead)"/>
    </g>
  </svg>

  <div class="node node--support node--secretary">Company<br>Secretary</div>
  <div class="node node--primary node--board">BOARD OF DIRECTORS</div>
  <div class="node node--primary node--management">MANAGEMENT</div>
  <div class="node node--support node--audit">Audit &amp;<br>Corporate<br>Risk</div>
  <div class="node node--support node--lending">Lending &amp;<br>Credit<br>Commitee</div>
  <div class="node node--support node--compliance">Compliance<br>Commitee</div>
</main>
</body>
</html>
```